Business card design needed

I would like a one sided black business card with the information provided above. Refer to my website www.lobcrafttennis.com.au for an example of colors I have used for my site, would like to keep this consistent for my business cards also, I will upload my logo below.

I am a new small business that provides tennis customers with racquet re stringing, tennis strings and accessories.

Industry/Entity Type

Small Business

Contact Information for Business Card

Lob Craft Tennis

Dennis Morrow
Managing Director

lobcrafttennis@mailbay.com
www.lobcrafttennis.com.au
0412 695 203

Racquet Restringing/Tennis Strings/Accessories

Requirements
Must have
• Must have my logo and card must be black

```html
<!DOCTYPE html>
<html lang="en">
<head>
<meta charset="UTF-8">
<title>Lob Craft Tennis – Business Card</title>
<link rel="stylesheet" href="https://fonts.googleapis.com/css2?family=Arimo:ital,wght@0,400;0,700;1,400&display=swap">
<style>
  :root {
    --canvas-bg: #ece9e4;
    --card-black: #000000;
    --card-white: #ffffff;
    --lime: #a6cc2e;
    --text-dark: #111111;
    --text-light: #ffffff;
    --rule-white: #d9d9d9;
  }
  * { margin: 0; padding: 0; box-sizing: border-box; }
  html, body {
    width: 1200px;
    height: 890px;
    overflow: hidden;
    background: var(--canvas-bg);
    font-family: "Arimo", Arial, sans-serif;
  }
  .canvas { position: relative; width: 1200px; height: 890px; }

  .card {
    position: absolute;
    overflow: hidden;
    box-shadow: 0 2px 6px rgba(0,0,0,0.25);
  }

  /* Front */
  .card-front {
    left: 63px; top: 133px;
    width: 610px; height: 357px;
    background: var(--card-black);
  }
  .brand-mark {
    position: absolute;
    display: flex;
    align-items: center;
    gap: 12px;
    transform: translate(-50%, -50%);
    white-space: nowrap;
  }
  .brand-dot {
    width: 30px; height: 30px;
    border-radius: 50%;
    background: var(--lime);
    flex: none;
  }
  .brand-name {
    color: var(--lime);
    font-weight: 700;
    text-transform: uppercase;
    letter-spacing: 1px;
  }
  .card-front .brand-mark { left: 300px; top: 165px; }
  .card-front .brand-name { font-size: 36px; }
  .tagline {
    position: absolute;
    left: 60px; top: 266px;
    width: 480px;
    text-align: center;
    color: var(--text-light);
    font-style: italic;
    font-size: 19px;
  }
  .edge-rules { position: absolute; top: 0; left: 540px; width: 40px; height: 357px; }

  /* Back */
  .card-back {
    left: 387px; top: 501px;
    width: 605px; height: 355px;
    background: var(--card-white);
    border: 1px solid #cfcfcf;
  }
  .holder-name {
    position: absolute; left: 31px; top: 22px;
    font-style: italic; font-size: 33px; color: var(--text-dark);
  }
  .holder-title {
    position: absolute; left: 31px; top: 62px;
    font-style: italic; font-size: 23px; color: var(--text-dark);
  }
  .contact-list {
    position: absolute; left: 296px; top: 110px;
    list-style: none;
  }
  .contact-item {
    display: flex; align-items: center; gap: 5px;
    height: 26.5px;
    font-style: italic; font-size: 19px; color: var(--text-dark);
  }
  .contact-item svg { width: 22px; height: 22px; flex: none; }
  .back-band {
    position: absolute; left: 0; top: 199px;
    width: 100%; height: 156px;
    background: var(--card-black);
  }
  .card-back .brand-mark { left: 295px; top: 64px; }
  .card-back .brand-name { font-size: 30px; }
  .card-back .brand-dot { width: 26px; height: 26px; }
  .accent-bar {
    position: absolute; left: 70px; bottom: 4px;
    width: 455px; height: 6px;
    border-radius: 3px;
    background: var(--lime);
  }
</style>
</head>
<body>
<main class="canvas">

  <section class="card card-front" aria-label="Card front">
    <div class="brand-mark">
      <span class="brand-dot"></span>
      <span class="brand-name">Lob Craft Tennis</span>
    </div>
    <p class="tagline">Racquet Restringing / Tennis Strings / Accessories</p>
    <svg class="edge-rules" viewBox="0 0 40 357" aria-hidden="true">
      <line x1="4" y1="0" x2="4" y2="357" stroke="var(--rule-white)" stroke-width="1.5"/>
      <line x1="13" y1="0" x2="13" y2="357" stroke="var(--lime)" stroke-width="2"/>
      <line x1="22" y1="0" x2="22" y2="357" stroke="var(--rule-white)" stroke-width="1.5"/>
      <line x1="30" y1="0" x2="30" y2="357" stroke="var(--lime)" stroke-width="2"/>
    </svg>
  </section>

  <section class="card card-back" aria-label="Card back">
    <h1 class="holder-name">Dennis Morrow</h1>
    <p class="holder-title">Managing Director</p>
    <ul class="contact-list">
      <li class="contact-item">
        <svg viewBox="0 0 24 24" aria-hidden="true">
          <circle cx="12" cy="12" r="10.5" fill="none" stroke="#222" stroke-width="1.6"/>
          <path d="M8.2 6.5c.6-.4 1.3-.3 1.6.3l1 1.8c.3.5.1 1.1-.3 1.4l-.7.5c.6 1.4 1.6 2.5 3 3.2l.5-.7c.3-.4 1-.6 1.4-.3l1.8 1c.6.3.7 1 .3 1.6-.8 1.1-2 1.6-3.3 1.1-3-1.1-5.2-3.4-6.3-6.4-.4-1.3.1-2.6 1-3.5z" fill="#222"/>
        </svg>
        <span>0412 695 203</span>
      </li>
      <li class="contact-item">
        <svg viewBox="0 0 24 24" aria-hidden="true">
          <rect x="2.5" y="5.5" width="19" height="13" fill="none" stroke="#222" stroke-width="1.6"/>
          <path d="M2.5 5.5l9.5 7.5 9.5-7.5M2.5 18.5l7-6M21.5 18.5l-7-6" fill="none" stroke="#222" stroke-width="1.4"/>
        </svg>
        <span>lobcrafttennis@mailbay.com</span>
      </li>
      <li class="contact-item">
        <svg viewBox="0 0 24 24" aria-hidden="true">
          <circle cx="12" cy="12" r="10.5" fill="none" stroke="#222" stroke-width="1.6"/>
          <circle cx="12" cy="12" r="3.2" fill="none" stroke="#222" stroke-width="1.8"/>
          <path d="M15.2 9v4.2c0 1.3 1.7 1.6 2.2.4.6-1.5.5-3.3-.3-4.7-1.6-2.7-5.2-3.6-7.9-1.9-2.7 1.6-3.5 5.2-1.8 7.8 1.5 2.4 4.6 3.3 7.2 2.2" fill="none" stroke="#222" stroke-width="1.6"/>
        </svg>
        <span>www.lobcrafttennis.com.au</span>
      </li>
    </ul>
    <div class="back-band">
      <div class="brand-mark">
        <span class="brand-dot"></span>
        <span class="brand-name">Lob Craft Tennis</span>
      </div>
      <span class="accent-bar"></span>
    </div>
  </section>

</main>
</body>
</html>
```